Lidia Vanta Catering
Complete Stationery Design
Lidia Vanta Catering - Chef / Catering
Creative Brief
Bright & Fun-filled
Corazon Belmiro
Director, Sales & Marketing
2nd Floor, Quintero Bldg., Saldivar Avenue near corner Lupine Street, Navotas, Metro Manila, Philippines 1490
cbelmiro@lidiavanta-example.ph
www.lidiavanta-example.ph
Lidia Vanta is a high end catering company. Our design is modern Victorian. Color dark red, black and white but we are open to other color suggestion. We need the ff: - business cards - A4 and letter size paper with matching letter envelopes - Folder that fits A4 and letter size envelop - Fax Cover - CD sticker and cover - Sticker label - Address Sticker Label - Paper Bag Design - Styro lunch box design - Tissue Napkin Design - Name Plate - Identification Card Design
Victorian design with our Logo in the middle

```html
<!DOCTYPE html>
<html lang="en">
<head>
<meta charset="utf-8">
<title>Lidia Vanta Catering – Business Card Options</title>
<link href="https://fonts.googleapis.com/css2?family=Open+Sans:ital,wght@0,400;0,600;1,400&display=swap" rel="stylesheet">
<style>
  :root {
    --sheet: #ffffff;
    --ink: #2a2a2a;
    --ink-soft: #555555;
    --paper-light: #ffffff;
    --paper-dark: #141414;
    --frame-grey-1: #7d7d7d;
    --frame-grey-2: #d6d6d6;
    --frame-red-1: #b3191f;
    --frame-red-2: #7c0e12;
    --ornament-light: #9a9a9a;
    --ornament-dark: #bdbdbd;
    --label: #3a3a3a;
  }
  * { box-sizing: border-box; margin: 0; padding: 0; }
  html, body { width: 1200px; height: 806px; overflow: hidden; background: var(--sheet); }
  body { position: relative; font-family: "Open Sans", Arial, sans-serif; color: var(--ink); }

  .card {
    position: absolute;
    width: 536px;
    height: 298px;
    text-align: center;
    box-shadow: 0 0 0 1px rgba(0,0,0,0.12);
  }
  .card--front-a { left: 72px;  top: 29px; }
  .card--front-b { left: 643px; top: 29px; }
  .card--back-a  { left: 72px;  top: 386px; background: var(--paper-light); }
  .card--back-b  { left: 643px; top: 386px; background: var(--paper-dark); }

  .card--framed {
    background: linear-gradient(90deg,
      var(--frame-grey-1) 0%, var(--frame-grey-2) 40%, var(--frame-grey-1) 76%,
      var(--frame-red-1) 78%, var(--frame-red-2) 100%);
    padding: 12px;
  }
  .card__panel {
    position: relative;
    width: 100%;
    height: 100%;
  }
  .card--front-a .card__panel { background: var(--paper-light); color: var(--ink); }
  .card--front-b .card__panel { background: var(--paper-dark); color: #f2f2f2; }

  .crest {
    position: absolute;
    left: 50%;
    transform: translateX(-50%);
    width: 150px;
    height: 34px;
    border-radius: 50% 50% 6px 6px;
  }
  .card--front-a .crest, .card--back-a .crest {
    background: linear-gradient(180deg, #d4d4d4, var(--ornament-light));
  }
  .card--front-b .crest, .card--back-b .crest {
    background: linear-gradient(180deg, #5a5a5a, var(--ornament-dark));
  }
  .card__panel .crest { top: 6px; }
  .card--back-a .crest, .card--back-b .crest { top: 66px; width: 160px; height: 38px; }

  .brand-name {
    position: absolute;
    left: 0; right: 0;
    font-weight: 400;
    font-size: 34px;
    letter-spacing: 1px;
    line-height: 1;
  }
  .card__panel .brand-name { top: 66px; }
  .card--back-a .brand-name { top: 140px; color: #333333; font-size: 38px; }
  .card--back-b .brand-name { top: 140px; color: #eeeeee; font-size: 38px; }

  .contact { position: absolute; left: 0; right: 0; top: 150px; line-height: 1.25; }
  .contact__name { font-style: italic; font-size: 17px; }
  .contact__title { font-size: 14px; margin-bottom: 8px; }
  .contact__address { font-size: 10.5px; }
  .contact__lines { font-size: 10.5px; margin-top: 6px; }
  .card--front-a .contact__address, .card--front-a .contact__lines { color: var(--ink-soft); }

  .option-label {
    position: absolute;
    font-size: 19px;
    letter-spacing: 2.5px;
    color: var(--label);
    font-variant: small-caps;
  }
  .option-label--front-a { left: 120px; top: 340px; }
  .option-label--front-b { left: 695px; top: 340px; }
  .option-label--back-a  { left: 130px; top: 705px; }
  .option-label--back-b  { left: 700px; top: 705px; }
</style>
</head>
<body>

  <section class="card card--framed card--front-a">
    <div class="card__panel">
      <div class="crest" role="img" aria-label="Victorian crest ornament above the company name"></div>
      <div class="brand-name">Lidia Vanta Catering</div>
      <div class="contact">
        <p class="contact__name">Corazon Belmiro</p>
        <p class="contact__title">Director, Sales &amp; Marketing</p>
        <p class="contact__address">2nd Floor, Quintero Bldg., Saldivar Avenue near corner<br>Lupine Street, Navotas, Metro Manila, Philippines 1490</p>
        <p class="contact__lines">P: +632 555 0142 | C: +63917 555 0198 | E: cbelmiro@lidiavanta-example.ph | www.lidiavanta-example.ph</p>
      </div>
    </div>
  </section>

  <section class="card card--framed card--front-b">
    <div class="card__panel">
      <div class="crest" role="img" aria-label="Victorian crest ornament above the company name"></div>
      <div class="brand-name">Lidia Vanta Catering</div>
      <div class="contact">
        <p class="contact__name">Corazon Belmiro</p>
        <p class="contact__title">Director, Sales &amp; Marketing</p>
        <p class="contact__address">2nd Floor, Quintero Bldg., Saldivar Avenue near corner<br>Lupine Street, Navotas, Metro Manila, Philippines 1490</p>
        <p class="contact__lines">P: +632 555 0142 | C: +63917 555 0198 | E: cbelmiro@lidiavanta-example.ph | www.lidiavanta-example.ph</p>
      </div>
    </div>
  </section>

  <section class="card card--back-a">
    <div class="crest" role="img" aria-label="Victorian crest ornament above the company name"></div>
    <div class="brand-name">Lidia Vanta Catering</div>
  </section>

  <section class="card card--back-b">
    <div class="crest" role="img" aria-label="Victorian crest ornament above the company name"></div>
    <div class="brand-name">Lidia Vanta Catering</div>
  </section>

  <p class="option-label option-label--front-a">Business Card Front Option A</p>
  <p class="option-label option-label--front-b">Business Card Front Option B</p>
  <p class="option-label option-label--back-a">Business Card Back Option A</p>
  <p class="option-label option-label--back-b">Business Card Back Option B</p>

</body>
</html>
```